Festive Sexy Winter Banner GIF

Make a Banner that will feature on our website www.PlumRelax.com for this Christmas - Maybe a little bit of animation but not overwhelming - Size of banner must be 713 X 70 Pixels and needs to be a .gif so We can just drop it in and it will work site wide

Target Market(s)

Adult

Industry/Entity Type

Adult

Requirements
Must have
• WORDING MUST BE - Plum Relax 1000's of UK Escorts & Massage Parlours
Nice to have
• Slight animation but not too much

```html
<!DOCTYPE html>
<html lang="en">
<head>
<meta charset="utf-8">
<title>Plum Relax – Festive Winter Banner</title>
<link rel="stylesheet" href="https://fonts.googleapis.com/css2?family=Fredoka:wght@600;700&family=Open+Sans:wght@400&display=swap">
<style>
  :root {
    --page-bg: #ffffff;
    --banner-navy: #1c1868;
    --banner-violet: #2a1f7a;
    --skin-light: #ecdcd9;
    --skin-mid: #d2b6b6;
    --skin-shade: #b99b9f;
    --ribbon-red: #c3161c;
    --ribbon-dark: #8e0d12;
    --title-ice: #b3dcf4;
    --title-edge: #4f86c6;
    --tagline-pink: #f27cd9;
    --tagline-edge: #ffffff;
    --snow: #ffffff;
    --sparkle: #e9f7ff;
    --sparkle-glow: #6fc6ff;
    --caption-ink: #111111;
  }
  * { margin: 0; padding: 0; box-sizing: border-box; }
  html, body {
    width: 1200px; height: 1000px; overflow: hidden;
    background: var(--page-bg);
  }
  .sheet { position: relative; width: 1200px; height: 1000px; }

  .banner {
    position: absolute; left: 0; width: 1200px; height: 118px;
    background: linear-gradient(90deg, var(--banner-navy) 0%, var(--banner-violet) 50%, var(--banner-violet) 56%);
    overflow: hidden;
  }
  .banner--frame-a { top: 125px; }
  .banner--frame-b { top: 293px; }

  .banner__photo {
    position: absolute; top: 0; right: 0; width: 640px; height: 118px;
    background: linear-gradient(90deg,
      rgba(42,31,122,0) 0%,
      rgba(120,100,160,0.6) 12%,
      var(--skin-mid) 24%,
      var(--skin-shade) 34%,
      var(--skin-light) 60%,
      var(--skin-mid) 78%,
      var(--skin-shade) 100%);
  }

  .banner__snow, .banner__sparkles {
    position: absolute; left: 0; top: 0; width: 1200px; height: 118px;
  }

  .banner__bow {
    position: absolute; left: 0; top: 0; width: 130px; height: 118px;
    background: linear-gradient(135deg,
      rgba(195,22,28,0) 18%,
      var(--ribbon-red) 34%,
      var(--ribbon-dark) 50%,
      var(--ribbon-red) 66%,
      rgba(195,22,28,0) 84%);
  }

  .banner__title {
    position: absolute; left: 252px; top: 22px;
    font-family: "Fredoka", sans-serif; font-weight: 700;
    font-size: 45px; line-height: 1; letter-spacing: 0.6px;
    color: var(--title-ice);
    text-shadow: 0 1px 0 var(--title-edge);
    white-space: nowrap;
  }

  .banner__tagline {
    position: absolute; left: 105px; top: 70px;
    font-family: "Fredoka", sans-serif; font-weight: 700;
    font-size: 26.5px; line-height: 1; letter-spacing: 0.2px;
    color: var(--tagline-pink);
    text-shadow: 0 0 2px var(--tagline-edge);
    white-space: nowrap;
  }

  .spec {
    position: absolute; left: 0; width: 1200px; text-align: center;
    font-family: "Open Sans", sans-serif; font-weight: 400;
    color: var(--caption-ink); text-transform: uppercase;
  }
  .spec--size { top: 636px; font-size: 25.5px; }
  .spec--output { top: 670px; font-size: 25.5px; }
  .spec--note { top: 724px; font-size: 20.5px; line-height: 30px; }
</style>
</head>
<body>
<main class="sheet">
  <svg width="0" height="0" style="position:absolute" aria-hidden="true">
    <defs>
      <filter id="soft-flake" x="-1" y="-1" width="3" height="3">
        <feGaussianBlur stdDeviation="0.8"/>
      </filter>
      <radialGradient id="sparkle-halo">
        <stop offset="0" stop-color="#ffffff" stop-opacity="1"/>
        <stop offset="0.35" stop-color="#6fc6ff" stop-opacity="0.7"/>
        <stop offset="1" stop-color="#6fc6ff" stop-opacity="0"/>
      </radialGradient>
      <g id="sparkle">
        <circle r="10" fill="url(#sparkle-halo)"/>
        <path d="M0 -22 L2 -2 L24 0 L2 2 L0 20 L-2 2 L-22 0 L-2 -2 Z" fill="#e9f7ff"/>
        <path d="M-7 -7 L0 -1 L7 -7 L1 0 L7 7 L0 1 L-7 7 L-1 0 Z" fill="#e9f7ff" opacity="0.8"/>
      </g>
    </defs>
  </svg>

  <section class="banner banner--frame-a" aria-label="Banner animation frame one">
    <div class="banner__photo" role="img" aria-label="Close-up photo of a woman's eyes with soft make-up"></div>
    <svg class="banner__snow" viewBox="0 0 1200 118" aria-hidden="true">
      <g fill="var(--snow)" filter="url(#soft-flake)">
        <circle cx="14" cy="30" r="3"/>
        <circle cx="77" cy="72" r="3"/>
        <circle cx="120" cy="18" r="2.5"/>
        <circle cx="168" cy="98" r="2.5"/>
        <circle cx="212" cy="110" r="3.5"/>
        <circle cx="232" cy="50" r="2"/>
        <circle cx="300" cy="104" r="2"/>
        <circle cx="396" cy="40" r="2"/>
        <circle cx="470" cy="110" r="2.5"/>
        <circle cx="517" cy="32" r="2.5"/>
        <circle cx="598" cy="12" r="2"/>
        <circle cx="625" cy="100" r="2"/>
        <circle cx="696" cy="24" r="2"/>
        <circle cx="946" cy="15" r="3"/>
        <circle cx="936" cy="72" r="2.5"/>
        <circle cx="1060" cy="104" r="2"/>
      </g>
    </svg>
    <div class="banner__bow" role="img" aria-label="Red gift ribbon bow in the corner"></div>
    <h1 class="banner__title">PLUM RELAX</h1>
    <p class="banner__tagline">1000'S OF UK ESCORTS &amp; MASSAGE PARLOURS</p>
    <svg class="banner__sparkles" viewBox="0 0 1200 118" aria-hidden="true">
      <use href="#sparkle" x="258" y="20"/>
      <use href="#sparkle" x="566" y="56"/>
    </svg>
  </section>

  <section class="banner banner--frame-b" aria-label="Banner animation frame two">
    <div class="banner__photo" role="img" aria-label="Close-up photo of a woman's eyes with soft make-up"></div>
    <svg class="banner__snow" viewBox="0 0 1200 118" aria-hidden="true">
      <g fill="var(--snow)" filter="url(#soft-flake)">
        <circle cx="28" cy="16" r="3"/>
        <circle cx="62" cy="52" r="2.5"/>
        <circle cx="124" cy="40" r="2.5"/>
        <circle cx="180" cy="22" r="3"/>
        <circle cx="194" cy="60" r="2.5"/>
        <circle cx="210" cy="92" r="2.5"/>
        <circle cx="294" cy="108" r="2.5"/>
        <circle cx="240" cy="40" r="2"/>
        <circle cx="418" cy="108" r="2"/>
        <circle cx="506" cy="16" r="2"/>
        <circle cx="572" cy="48" r="2"/>
        <circle cx="640" cy="96" r="2.5"/>
        <circle cx="913" cy="25" r="3"/>
        <circle cx="984" cy="96" r="2"/>
        <circle cx="850" cy="110" r="2"/>
      </g>
    </svg>
    <div class="banner__bow" role="img" aria-label="Red gift ribbon bow in the corner"></div>
    <h2 class="banner__title">PLUM RELAX</h2>
    <p class="banner__tagline">1000'S OF UK ESCORTS &amp; MASSAGE PARLOURS</p>
    <svg class="banner__sparkles" viewBox="0 0 1200 118" aria-hidden="true">
      <use href="#sparkle" x="258" y="18"/>
    </svg>
  </section>

  <p class="spec spec--size">Size: 713 x 70 pixels</p>
  <p class="spec spec--output">Final product: GIF file with animation of 2 stars (A and E) and snow</p>
  <p class="spec spec--note">( Preview banner is JPEG file because can’t upoad file GIF<br>but can download GIF file in source file. )</p>
</main>
</body>
</html>
```